Bref créative
Business Card for Real Estate Company
Larkfield Residences
Professional
Marcy Dunwell
Realtor
248 E. Corwin Ave. Suite 716
Anchorage, Alaska 40817
larkfieldtx@mailvista.example
www.larkfieldtx.example
Its a card for a Norcott Praine Realtor. Make sure in small print somewhere on card its states "Each Office Independently Owned and Operated"

```html
<!DOCTYPE html>
<html lang="en">
<head>
<meta charset="utf-8">
<title>Larkfield Residences – Business Card</title>
<link href="https://fonts.googleapis.com/css2?family=Open+Sans:ital,wght@0,400;0,600;0,700;1,700&display=swap" rel="stylesheet">
<style>
  :root {
    --brand-red: #a01c2a;
    --brand-grey: #6b6c70;
    --ink-soft: #8a8b8f;
    --card-white: #ffffff;
    --page-bg: #e9e7e4;
  }
  * { margin: 0; padding: 0; box-sizing: border-box; }
  html, body {
    width: 1200px;
    height: 914px;
    overflow: hidden;
    background: var(--page-bg);
    font-family: "Open Sans", Arial, sans-serif;
  }
  .stage {
    width: 1200px;
    height: 914px;
    display: flex;
    align-items: center;
    justify-content: center;
  }
  .business-card {
    position: relative;
    width: 900px;
    height: 514px;
    background: var(--card-white);
    box-shadow: 0 6px 24px rgba(0,0,0,0.12);
  }
  .brand-mark {
    position: absolute;
    top: 92px;
    left: 0;
    right: 0;
    display: flex;
    align-items: center;
    justify-content: center;
    gap: 14px;
  }
  .brand-square {
    width: 26px;
    height: 26px;
    background: var(--brand-red);
  }
  .brand-name {
    font-size: 38px;
    font-weight: 600;
    letter-spacing: 1px;
    text-transform: uppercase;
    color: var(--brand-red);
  }
  .brokerage-tab {
    position: absolute;
    left: 0;
    top: 148px;
    width: 62px;
    height: 150px;
    background: var(--brand-red);
    display: flex;
    align-items: center;
    justify-content: center;
  }
  .brokerage-name {
    transform: rotate(-90deg);
    white-space: nowrap;
    color: var(--card-white);
    font-size: 13px;
    font-weight: 700;
    letter-spacing: 1px;
    text-transform: uppercase;
  }
  .brokerage-box {
    position: absolute;
    left: 62px;
    top: 148px;
    width: 14px;
    height: 150px;
    background: #d9d9db;
  }
  .contact-block {
    position: absolute;
    left: 92px;
    top: 196px;
    font-size: 11.5px;
    line-height: 1.55;
    color: var(--brand-grey);
  }
  .disclaimer {
    position: absolute;
    left: 92px;
    bottom: 26px;
    font-size: 9px;
    color: var(--ink-soft);
  }
  .agent {
    position: absolute;
    right: 40px;
    bottom: 62px;
    text-align: right;
  }
  .agent-name {
    font-size: 30px;
    font-weight: 700;
    font-style: italic;
    color: var(--brand-red);
  }
  .agent-title {
    font-size: 22px;
    font-weight: 400;
    color: var(--brand-grey);
    margin-top: 2px;
  }
</style>
</head>
<body>
  <main class="stage">
    <section class="business-card" aria-label="Larkfield Residences business card">
      <div class="brand-mark">
        <span class="brand-square" aria-hidden="true"></span>
        <span class="brand-name">Larkfield Residences</span>
      </div>

      <div class="brokerage-tab"><span class="brokerage-name">Norcott Praine</span></div>
      <div class="brokerage-box" aria-hidden="true"></div>

      <address class="contact-block" style="font-style: normal;">
        248 E. Corwin Ave. Suite 716<br>
        Anchorage, Alaska 40817<br>
        Office 555 014 2208<br>
        Cell 555 014 7731<br>
        larkfieldtx@mailvista.example<br>
        www.larkfieldtx.example
      </address>

      <p class="disclaimer">Each Office Independently Owned and Operated</p>

      <div class="agent">
        <p class="agent-name">Marcy Dunwell</p>
        <p class="agent-title">Realtor</p>
      </div>
    </section>
  </main>
</body>
</html>
```